Membership, training, certification programs

4 pages brochure

1. An overview of the association:
http://www.norvane-guild-hub.org

"The Norvane Risk Practitioners Guild (NRPG) is the largest association of Basel iii Professionals in the world. It is a business unit of the Kellmoor Risk Practitioners Guild (KRPG), which is also the largest association of Basel ii Professionals in the world"

2. Reading Room
http://www.norvane-guild-hub.org/Reading_Room.html

3. Basel iii - Distance Learning and Online Certification Programs
http://www.norvane-guild-hub.org/Guild_Distance_Learning_Online_Certification.html

4. Authorized Certified Trainer (NRPG-ACT)
http://www.norvane-guild-hub.org/NRPG_ACT.html

Overview

We need to print the brochure at Printholm

Thank you

4 pages brochure 1st page. An overview of the association: http://www.norvane-guild-hub.org "The Norvane Risk Practitioners Guild (NRPG) is the largest association of Basel iii Professionals in the world. It is a business unit of the Kellmoor Risk Practitioners Guild (KRPG), which is also the largest association of Basel ii Professionals in the world" 2nd page. Reading Room http://www.norvane-guild-hub.org/Reading_Room.html 3rd page. Basel iii - Distance Learning and Online Certification Programs http://www.norvane-guild-hub.org/Guild_Distance_Learning_Online_Certification.html 4th page. Authorized Certified Trainer (NRPG-ACT) and Contact us http://www.norvane-guild-hub.org/NRPG_ACT.html Overview We need to print the brochure at Printholm Thank you

Target Market(s)

Risk managers

Industry/Entity Type

Business

Colors
0255a3
eb1f27

Requirements
Must have
• Serious, short descriptions of the 4 areas

```html
<!DOCTYPE html>
<html lang="en">
<head>
<meta charset="utf-8">
<title>Basel iii - Distance Learning and Online Certification Programs</title>
<link href="https://fonts.googleapis.com/css2?family=Open+Sans:wght@400;600;700&display=swap" rel="stylesheet">
<style>
:root{
  --red:#eb1f27;
  --blue:#0255a3;
  --ink:#231f20;
  --white:#ffffff;
}
*{margin:0;padding:0;box-sizing:border-box}
html,body{width:929px;height:1200px;overflow:hidden;background:var(--white)}
body{font-family:"Open Sans",Arial,sans-serif;color:var(--ink);position:relative}
.masthead{position:absolute;left:0;top:0;width:929px;height:127px;background:var(--red)}
.masthead h1{position:absolute;left:52px;top:47px;color:var(--white);font-size:26px;line-height:32px;font-weight:700}
.rule-blue{position:absolute;left:0;top:129px;width:929px;height:8px;background:var(--blue)}
.offer-panel{position:absolute;left:0;top:162px;width:877px;height:252px;background:var(--red);color:var(--white);padding:26px 0 0 52px;font-size:16.5px;line-height:18.5px}
.offer-side{position:absolute;left:877px;top:162px;width:52px;height:252px;background:var(--blue)}
.offer{margin-bottom:17px}
.offer strong{font-weight:700}
.content{position:absolute;left:52px;top:451px;width:832px;font-size:13.3px;line-height:18px}
.content h2,.content h3{font-size:13.3px;font-weight:700}
.content p{margin-bottom:17px}
.block{margin-bottom:17px}
.steps li{list-style:none;padding-left:58px;text-indent:-58px}
.steps b{font-weight:700}
.bullets li{list-style:none}
.footer{position:absolute;left:0;top:1105px;width:929px;height:95px;background:var(--blue);color:var(--white);font-size:12.5px;line-height:16px;padding:19px 0 0 52px}
.footer b{font-weight:700}
.footer-photo{position:absolute;left:548px;top:1105px;width:381px;height:95px;
  background:linear-gradient(180deg,#1a2a4a 0%,#3a4a6a 45%,#8a7350 75%,#2a2a30 100%);
  clip-path:polygon(22px 0,100% 0,100% 100%,0 100%)}
.footer-slash{position:absolute;left:548px;top:1105px;width:30px;height:95px;background:var(--white);clip-path:polygon(22px 0,26px 0,4px 100%,0 100%)}
</style>
</head>
<body>
<header class="masthead">
  <h1>Basel iii - Distance Learning and<br>Online Certification Programs</h1>
</header>
<div class="rule-blue"></div>

<section class="offer-panel">
  <div class="offer"><strong>Certified Basel iii Professional (CNRPro)<br>Distance Learning and Online Certification Program</strong><br>The all inclusive cost is <strong>$297</strong></div>
  <div class="offer"><strong>Certified Basel iii Professional (CNRPro) and Certified Basel ii Professional (CKRPro)</strong><br>2 Distance Learning and Online Certification Programs, 2 Professional Certificates<br>The all inclusive cost is <strong>$473</strong></div>
  <div class="offer"><strong>CKRPro, CPXE, CPYE, CSRE and CNRPro</strong><br>5 Distance Learning and Online Certification Programs, 5 Professional Certificates<br>The all inclusive cost is <strong>$797</strong></div>
</section>
<div class="offer-side"></div>

<main class="content">
  <div class="block">
    <h2>Norvane Risk Practitioners Guild (NRPG)</h2>
    The Norvane Risk Practitioners Guild (NRPG) is a business unit of the Kellmoor Risk Practitioners Guild (KRPG), the largest association of Basel ii Professionals in the world.
  </div>
  <div class="block"><h2>Basel iii - Distance Learning and Online Certification Programs</h2></div>
  <div class="block">
    <h3>Certified Basel iii Professional (CNRPro)</h3>
    Distance Learning and Online Certification Program<br>
    The all inclusive cost is <b>$297</b>
  </div>
  <div class="block">
    <h3>What is included in this price:</h3>
    <ul class="bullets">
      <li>• The official presentations we use in our instructor-led classes (about 2,600 slides)</li>
      <li>• Up to 3 Online Exams</li>
      <li>• Personalized Certificate printed in full colour</li>
    </ul>
  </div>
  <div class="block">
    <h3>STEPS - To become Certified Basel iii Professional (CNRPro)</h3>
    <ul class="steps">
      <li><b>Step 1</b> - For secure payment we use Quillvarro Checkout.</li>
      <li><b>Step 2</b> - We will send you the official presentations via email in less than 48 hours.</li>
      <li><b>Step 3</b> - When you feel ready to sit for the exam, please send an email to: Maren Holloway, Email: maren@norvane-guild-hub.org</li>
      <li><b>Step 4</b> - If you pass, congratulations. You will learn it immediately after the exam.</li>
      <li><b>Step 5</b> - We will send to your mail address a Personalized Certificate printed in full color. It will take 6 - 8 weeks.</li>
      <li><b>Step 6</b> - If you do not pass the exam: Study the presentation we have sent you. Try to understand the details. You will have the opportunity to try again.</li>
      <li><b>Step 7</b> - You will have (at no extra cost) a second opportunity to sit for the exam. You can use the same Username, Password and Account information we have sent you.</li>
      <li><b>Step 8</b> - If you do not pass again, you have to study more.</li>
      <li><b>Step 9</b> - If you do not pass, you will have (at no extra cost) another opportunity to sit for the exam, but you have to study and learn more. After one year, you can try again (for the 4th time).</li>
    </ul>
  </div>
  <div class="block">
    To learn more you may visit:<br>
    <b>www.norvane-guild-hub.org/Questions_About_The_Certification_And_The_Exams_1.pdf</b><br>
    or <b>www.norvane-guild-hub.org/Certification_Steps_CNRPro.pdf</b>
  </div>
  <p>For any questions please contact Maren Holloway, <b>Email: maren@norvane-guild-hub.org</b></p>
</main>

<footer class="footer">
  <b>Norvane Risk Practitioners Guild (NRPG)</b><br>
  410 Alder Row Suite 300, Carrow City 20417, USA<br>
  <b>Tel</b> (202) 555-0148 | <b>Email</b> Maren Holloway at maren@norvane-guild-hub.org<br>
  <b>Web</b> www.norvane-guild-hub.org
</footer>
<div class="footer-photo" role="img" aria-label="Night view of an old European city skyline with church spires along a lakefront"></div>
<div class="footer-slash"></div>
</body>
</html>
```